continued... Web Design for Professional Development and marketplace

in addition to the homepages that you are desiging, can you also create designs for the attached wireframes that are part of the same website.
I am creating this as a seperate project as we are keen to see your designs for the rest of the website.
VIdeo of prototype and homepage designs
https://www.quellbin.net/sh/rk8tp2mqvx41hwa/7Gt3oLnQ2z/design
Updates
added an additional wireframe that was missed in the original upload
added one more wireframe for the homepage: where the user is prompted to login or signup
Industry/Entity Type
Marketplace
Look and feel
Each slider illustrates characteristics of the customer's brand and the style your logo design should communicate.

```html
<!DOCTYPE html>
<html lang="en">
<head>
<meta charset="utf-8">
<title>Competency Planning Tool – Harwell School of Business</title>
<link rel="stylesheet" href="https://fonts.googleapis.com/css2?family=Open+Sans:wght@400;600;700&display=swap">
<style>
  :root {
    --header-bg: #2b2f38;
    --header-btn: #545b65;
    --accent: #f39c12;
    --accent-text: #e5890e;
    --white: #ffffff;
    --text-dark: #333840;
    --text-mid: #555a60;
    --text-light: #70757a;
    --muted: #9a9ea3;
    --border: #d6d8da;
    --icon: #c3c6c9;
  }
  * { box-sizing: border-box; margin: 0; padding: 0; }
  html, body { width: 1200px; height: 706px; overflow: hidden; background: var(--white); }
  body { font-family: "Open Sans", Arial, sans-serif; position: relative; }

  .site-header { position: absolute; top: 0; left: 0; width: 1200px; height: 81px; background: var(--header-bg); }
  .menu-button { position: absolute; left: 110px; top: 15px; width: 58px; height: 47px; background: var(--header-btn); border-radius: 3px; display: flex; align-items: center; justify-content: center; }
  .search { position: absolute; left: 170px; top: 15px; width: 213px; height: 47px; display: flex; }
  .search-input { width: 163px; height: 47px; background: var(--white); border-radius: 3px 0 0 3px; padding: 0 13px; font-size: 16px; color: var(--muted); line-height: 47px; }
  .search-button { width: 50px; height: 47px; background: var(--header-btn); border-radius: 0 3px 3px 0; display: flex; align-items: center; justify-content: center; }
  .brand { position: absolute; left: 450px; top: 8px; width: 300px; text-align: center; color: var(--white); }
  .brand-name { font-size: 31px; font-weight: 600; line-height: 40px; letter-spacing: 0.2px; }
  .brand-sub { font-size: 19px; line-height: 20px; }
  .auth-links { position: absolute; left: 746px; top: 31px; font-size: 13px; font-weight: 700; color: var(--white); }
  .auth-links .or { color: #7d828a; font-weight: 600; margin-left: 4px; }
  .login-button { position: absolute; left: 826px; top: 15px; width: 106px; height: 47px; background: var(--header-btn); border-radius: 3px; color: var(--white); font-size: 16px; font-weight: 600; display: flex; align-items: center; justify-content: center; gap: 9px; }
  .review-button { position: absolute; left: 934px; top: 15px; width: 155px; height: 47px; background: var(--accent); border-radius: 3px; color: var(--white); font-size: 15px; font-weight: 600; display: flex; align-items: center; justify-content: center; gap: 8px; }

  .sub-nav { position: absolute; top: 81px; left: 0; width: 1200px; height: 32px; background: var(--accent); }
  .sub-nav ul { list-style: none; position: absolute; right: 110px; top: 6px; display: flex; gap: 28px; }
  .sub-nav li { color: var(--white); font-size: 14px; line-height: 20px; }

  .filter-bar { position: absolute; left: 109px; top: 120px; width: 982px; height: 70px; border: 1px solid var(--border); display: flex; box-shadow: 0 1px 2px rgba(0,0,0,0.06); }
  .filter { border-left: 1px solid var(--border); text-align: center; padding-top: 8px; }
  .filter:first-child { border-left: none; }
  .filter-icon { height: 16px; display: flex; justify-content: center; }
  .filter-label { font-size: 15px; color: var(--text-mid); line-height: 19px; }
  .filter-value { font-size: 12px; color: var(--accent-text); line-height: 18px; }
  .filter-save { background: var(--accent); color: var(--white); font-weight: 700; font-size: 15px; padding-top: 15px; }

  .page-title { position: absolute; left: 108px; top: 221px; font-size: 29px; font-weight: 700; color: var(--accent-text); }
  .page-intro { position: absolute; left: 108px; top: 260px; font-size: 16px; color: var(--text-mid); }
  .divider { position: absolute; left: 109px; top: 295px; width: 981px; height: 1px; background: #dcdedf; }

  .section-title { position: absolute; left: 107px; top: 336px; font-size: 21px; font-weight: 600; color: var(--text-dark); }
  .field { position: absolute; left: 108px; width: 540px; height: 33px; display: flex; align-items: center; }
  .field-label { width: 213px; font-size: 14px; color: var(--text-light); }
  .select { width: 327px; height: 33px; border: 1px solid #c5c8cb; border-radius: 3px; position: relative; font-size: 13px; color: var(--muted); line-height: 31px; padding-left: 9px; box-shadow: inset 0 1px 2px rgba(0,0,0,0.05); }
  .select::after { content: ""; position: absolute; right: 32px; top: 6px; width: 1px; height: 20px; background: #d2d4d6; }
  .select-caret { position: absolute; right: 13px; top: 14px; }

  .next-button { position: absolute; left: 109px; top: 538px; width: 217px; height: 47px; background: var(--accent); border-radius: 2px; color: var(--white); font-size: 15px; font-weight: 600; display: flex; align-items: center; padding-left: 19px; gap: 17px; }
</style>
</head>
<body>
  <header class="site-header">
    <div class="menu-button">
      <svg width="34" height="24" viewBox="0 0 34 24"><rect y="0" width="34" height="4" fill="#fff"/><rect y="10" width="34" height="4" fill="#fff"/><rect y="20" width="34" height="4" fill="#fff"/></svg>
    </div>
    <div class="search">
      <div class="search-input">Search</div>
      <div class="search-button">
        <svg width="22" height="22" viewBox="0 0 22 22"><circle cx="9" cy="9" r="6.5" fill="none" stroke="#fff" stroke-width="3"/><line x1="13.5" y1="13.5" x2="20" y2="20" stroke="#fff" stroke-width="3.5" stroke-linecap="round"/></svg>
      </div>
    </div>
    <div class="brand">
      <div class="brand-name">Harwell School</div>
      <div class="brand-sub">of Business</div>
    </div>
    <div class="auth-links">Sign Up <span class="or">or</span></div>
    <div class="login-button">
      <svg width="20" height="22" viewBox="0 0 20 22"><circle cx="10" cy="6" r="5.5" fill="#fff"/><path d="M0 22c0-6 4-9 10-9s10 3 10 9z" fill="#fff"/></svg>
      Login
    </div>
    <div class="review-button">
      <svg width="28" height="24" viewBox="0 0 28 24"><path d="M2 2h20v14H9l-5 4v-4H2z" fill="none" stroke="#fff" stroke-width="1.8"/><line x1="6" y1="7" x2="18" y2="7" stroke="#fff" stroke-width="1.5"/><line x1="6" y1="11" x2="14" y2="11" stroke="#fff" stroke-width="1.5"/><circle cx="22" cy="17" r="5.5" fill="#fff"/><path d="M22 14v6M19 17h6" stroke="#f39c12" stroke-width="1.8"/></svg>
      Add Review
    </div>
  </header>

  <nav class="sub-nav">
    <ul>
      <li>About</li><li>Business</li><li>Developers</li><li>Pricacy &amp; Terms</li><li>Copyright &amp; Trademark</li>
    </ul>
  </nav>

  <div class="filter-bar">
    <div class="filter filter-save" style="width:100px">
      <div class="filter-icon"><svg width="15" height="15" viewBox="0 0 15 15"><rect x="1" y="1" width="13" height="13" rx="1.5" fill="none" stroke="#fff" stroke-width="2"/><rect x="4" y="1" width="7" height="4" fill="#fff"/></svg></div>
      Save
    </div>
    <div class="filter" style="width:88px">
      <div class="filter-icon"><svg width="16" height="14" viewBox="0 0 16 14"><rect x="1" y="4" width="14" height="9" rx="1.5" fill="#c3c6c9"/><rect x="5" y="1" width="6" height="4" rx="1" fill="none" stroke="#c3c6c9" stroke-width="1.5"/></svg></div>
      <div class="filter-label">Career</div><div class="filter-value">(all)</div>
    </div>
    <div class="filter" style="width:132px">
      <div class="filter-icon"><svg width="15" height="14" viewBox="0 0 15 14"><path d="M1 1h13v9H6l-3 3v-3H1z" fill="#c3c6c9"/></svg></div>
      <div class="filter-label">Specialization</div><div class="filter-value">(all)</div>
    </div>
    <div class="filter" style="width:110px">
      <div class="filter-icon"><svg width="14" height="15" viewBox="0 0 14 15"><path d="M7 1a4 4 0 0 1 4 4c0 3-4 7-4 7S3 8 3 5a4 4 0 0 1 4-4z" fill="#c3c6c9"/><ellipse cx="7" cy="13" rx="6" ry="1.6" fill="#c3c6c9"/></svg></div>
      <div class="filter-label">Location</div><div class="filter-value">(Vancouver)</div>
    </div>
    <div class="filter" style="width:119px">
      <div class="filter-icon"><svg width="15" height="15" viewBox="0 0 15 15"><circle cx="7.5" cy="7.5" r="7" fill="#c3c6c9"/><text x="7.5" y="11" font-size="10" font-family="Open Sans, sans-serif" font-weight="700" fill="#fff" text-anchor="middle">$</text></svg></div>
      <div class="filter-label">Price</div><div class="filter-value">($600-$3000)</div>
    </div>
    <div class="filter" style="width:115px">
      <div class="filter-icon"><svg width="14" height="15" viewBox="0 0 14 15"><rect x="1" y="2" width="12" height="12" rx="1" fill="none" stroke="#c3c6c9" stroke-width="1.5"/><rect x="1" y="2" width="12" height="3" fill="#c3c6c9"/><text x="7" y="12.5" font-size="6" font-family="Open Sans, sans-serif" fill="#c3c6c9" text-anchor="middle">31</text></svg></div>
      <div class="filter-label">Start Date</div><div class="filter-value">(2-6 months)</div>
    </div>
    <div class="filter" style="width:123px">
      <div class="filter-icon"><svg width="16" height="14" viewBox="0 0 16 14"><rect x="1" y="9" width="4" height="5" fill="#c3c6c9"/><rect x="6" y="5" width="4" height="9" fill="#c3c6c9"/><rect x="11" y="1" width="4" height="13" fill="#c3c6c9"/></svg></div>
      <div class="filter-label">Level</div><div class="filter-value">(intermediate)</div>
    </div>
    <div class="filter" style="width:96px">
      <div class="filter-icon"><svg width="15" height="15" viewBox="0 0 15 15"><path d="M7.5 1 14 4v7l-6.5 3L1 11V4z M1 4l6.5 3L14 4 M7.5 7v7" fill="none" stroke="#c3c6c9" stroke-width="1.3"/></svg></div>
      <div class="filter-label">Type</div><div class="filter-value">(multiple)</div>
    </div>
    <div class="filter" style="width:97px">
      <div class="filter-icon"><svg width="16" height="16" viewBox="0 0 16 16"><circle cx="8" cy="7" r="3.5" fill="#c3c6c9"/><rect x="6.5" y="10.5" width="3" height="3" fill="#c3c6c9"/><path d="M8 0v2M2 7H0M16 7h-2M3 2l1.4 1.4M13 2l-1.4 1.4" stroke="#c3c6c9" stroke-width="1.2"/></svg></div>
      <div class="filter-label">Provider</div><div class="filter-value">(one)</div>
    </div>
  </div>

  <h1 class="page-title">Competency Planning Tool</h1>
  <p class="page-intro">Get recommendations for the best courses for you by completing a quick self evaluation</p>
  <div class="divider"></div>

  <h2 class="section-title">Desired Career</h2>
  <div class="field" style="top:396px">
    <span class="field-label">Select desired career:</span>
    <div class="select">Desired career<svg class="select-caret" width="7" height="4" viewBox="0 0 7 4"><path d="M0 0h7L3.5 4z" fill="#555"/></svg></div>
  </div>
  <div class="field" style="top:448px">
    <span class="field-label">Select desired specialisation:</span>
    <div class="select">Desired specialisation<svg class="select-caret" width="7" height="4" viewBox="0 0 7 4"><path d="M0 0h7L3.5 4z" fill="#555"/></svg></div>
  </div>

  <div class="next-button">
    Next, rate your skills
    <svg width="14" height="24" viewBox="0 0 14 24"><path d="M2 2l10 10L2 22" fill="none" stroke="#fff" stroke-width="2.5"/></svg>
  </div>
</body>
</html>
```